Cat-products company needs smart, yet endearing, business card

We need a business card design for a new, but up-and-running, business based in Honolulu, Hawaii. The business is Purrlane Nest Co. Our first product is the most environmentally-friendly cat grass kit ever seen on the planet. Future products, currently in the R&D phase, will include a variety of exciting cat scratchers. We also do consulting work to help apartment-dwellers make their home more cat-friendly and, in the future, plan on doing full, custom installs of structure to create high walkways for cats.

Target Market(s)

Middle-aged, apartment-dwelling, middle-class workers who own 1 or more cats and who dote on them.

Industry/Entity Type

Pet Care

Contact Information for Business Card

A striking, professional, yet warm and friendly design is what we're after.

Font styles to use
Serif
Sans Serif
Other font styles liked:
• Comfortaa

Colors

Designer to choose colors to be used in the design.

Requirements
Must have
• The company logo: (see attachment)
• The company name: Purrlane Nest Co
• The web address: www.purrlanenestco.example
• Email: support@purrlanenestco.example
• Phone: +1 (808) 555 0172
• Update (Fri Jun 30 3017 7:45pm Hawaii Time) I would like, is possible, uploaded picture of the cat grass kit on the back of the card with some text along the lines of: Purrlane Nest Co - Where The Freshest Kitty Sprouts Begin
Nice to have
• A cat picture, cartoon, real or silhouette that illustrates cats in action and/or relaxing; ie using the apartment space to live, play and relax in and being well-contented.
• Most of the website is done in the font: Comfortaa. It might be nice to continue using this for brand consistency.
Should not have
• Hard-to-read fonts.

```html
<!DOCTYPE html>
<html lang="en">
<head>
<meta charset="utf-8">
<title>Purrlane Nest Co — Business Card</title>
<link href="https://fonts.googleapis.com/css2?family=Comfortaa:wght@400;700&display=swap" rel="stylesheet">
<style>
  :root {
    --backdrop: #d6d6d6;
    --cocoa: #573330;
    --cocoa-deep: #4b2c29;
    --cocoa-soft: #613935;
    --sun: #f9b219;
    --paper: #ffffff;
    --ink: #3b2522;
    --fur: #161413;
    --fur-light: #2a2522;
  }
  * { box-sizing: border-box; margin: 0; padding: 0; }
  html, body {
    width: 1200px; height: 1200px; overflow: hidden;
    background: var(--backdrop);
    font-family: "Comfortaa", sans-serif;
  }
  .sheet {
    width: 1200px; height: 1200px;
    display: flex; flex-direction: column; align-items: center; justify-content: center;
    gap: 56px;
  }
  .card {
    position: relative;
    width: 900px; height: 514px;
    overflow: hidden;
    box-shadow: 0 6px 18px rgba(0,0,0,0.18);
  }

  /* Back side */
  .card--back { background: var(--cocoa); }
  .back-photo {
    position: absolute; right: 0; top: 0;
    width: 440px; height: 420px;
    border-bottom-left-radius: 220px;
    background: linear-gradient(160deg, var(--cocoa-deep) 0%, var(--cocoa-deep) 60%, var(--cocoa) 100%);
  }
  .back-paws {
    position: absolute; left: 310px; top: 170px;
    width: 150px; height: 300px;
    border-radius: 75px;
    background: var(--cocoa-soft);
    opacity: 0.55;
  }
  .brand {
    position: absolute;
    display: flex; align-items: center; gap: 14px;
    font-weight: 700; font-size: 36px; letter-spacing: 0.5px;
    white-space: nowrap;
  }
  .brand__dot { width: 34px; height: 34px; border-radius: 50%; background: var(--sun); flex: none; }
  .card--back .brand { left: 70px; top: 320px; color: var(--paper); }
  .tagline {
    position: absolute; left: 118px; top: 376px;
    font-size: 16px; font-weight: 700; color: var(--sun);
    white-space: nowrap;
  }

  /* Front side */
  .card--front { background: var(--paper); }
  .front-swoosh { position: absolute; inset: 0; }
  .card--front .brand { left: 80px; top: 250px; color: var(--cocoa); }
  .contact {
    position: absolute; left: 470px; top: 90px;
    list-style: none;
    display: flex; flex-direction: column; gap: 12px;
    font-size: 17px; color: var(--ink);
  }
  .contact li { display: flex; align-items: center; gap: 12px; }
  .contact svg { width: 20px; height: 20px; flex: none; }
  .front-paw {
    position: absolute; left: 790px; top: 186px;
    width: 72px; height: 64px;
    border-radius: 32px 32px 36px 36px;
    background: var(--sun);
  }
  .front-photo {
    position: absolute; left: 520px; top: 268px;
    width: 320px; height: 150px;
    border-radius: 75px;
    background: linear-gradient(135deg, var(--fur-light) 0%, var(--fur) 55%, var(--fur) 100%);
  }
</style>
</head>
<body>
<main class="sheet">

  <section class="card card--back" aria-label="Card back">
    <div class="back-photo" role="img" aria-label="Faint photo of a black cat stretching its paw"></div>
    <div class="back-paws" role="img" aria-label="Faint trail of heart-shaped paw prints"></div>
    <div class="brand"><span class="brand__dot"></span>Purrlane Nest Co</div>
    <p class="tagline">Where The Freshest Kitty Sprouts Begin</p>
  </section>

  <section class="card card--front" aria-label="Card front">
    <svg class="front-swoosh" viewBox="0 0 900 514" preserveAspectRatio="none" aria-hidden="true">
      <path d="M180 514 C 420 400, 760 330, 900 110 L 900 514 Z" fill="var(--sun)"/>
    </svg>
    <div class="brand"><span class="brand__dot"></span>Purrlane Nest Co</div>
    <ul class="contact">
      <li>
        <svg viewBox="0 0 20 20"><circle cx="10" cy="10" r="8" fill="none" stroke="var(--sun)" stroke-width="2"/><path d="M2 10h16M10 2c-3 3-3 13 0 16M10 2c3 3 3 13 0 16" fill="none" stroke="var(--sun)" stroke-width="1.5"/></svg>
        www.purrlanenestco.example
      </li>
      <li>
        <svg viewBox="0 0 20 20"><rect x="2" y="4" width="16" height="12" fill="var(--sun)"/><path d="M2 4l8 7 8-7" fill="none" stroke="var(--paper)" stroke-width="1.5"/></svg>
        support@purrlanenestco.example
      </li>
      <li>
        <svg viewBox="0 0 20 20"><path d="M3 8c0-3 14-3 14 0v2h-4V8H7v2H3z" fill="var(--sun)"/><rect x="5" y="11" width="10" height="6" rx="1" fill="var(--sun)"/></svg>
        +1 (808) 555 0172
      </li>
    </ul>
    <div class="front-paw" role="img" aria-label="Large yellow paw print"></div>
    <div class="front-photo" role="img" aria-label="Photo of a black cat lying playfully on its back"></div>
  </section>

</main>
</body>
</html>
```